Four Quiet Steps Toward a Stronger Offer on THE Property - VARN Real Estate

I have written an E-Book that is called "Four Quiet Steps Toward a Stronger Offer on The Property." The E-Book will be available as a FREE download from my VARN Real Estate landing page, and also from a Chatterbox campaign that will be commencing in early September.

The E-Book content is in the WORD document below - I now need for it to be made to look more professional and suitable for publishing and placed on my landing page for download. Please review and send me some proposals for this e-book to be a bit more eye catching and appealing than just a WORD doc.

My VARN Real Estate landing page is still under development and you can see the what is close to the final proposal here:

http://www.plum-orbit.com.au/varn/

The cover of the E-Book is at the bottom of the page. Please review and give the internals the sale look and feel.

Target Market(s)

Home and Property Owners in the middle ring Eastern Suburbs of Melbourne - approximately 15 - 30 km's from the central business district. The area is a very family oriented area and features mostly houses that are 3 or 4 bedroom - with some larger properties that are five or more bedrooms. The area is quite an expensive suburban community and house prices range between the low of $1,000,000 to a high of more than $2,500,000. The predominant cultural group that buys in this area are Chinese and Chinese Australian buyers. The predominant group who are selling are usually Australians of a white anglo-saxon background. Other groups are of Asian sub continent background (Indian / Sri Lankan/ Pakistan). All are families that are attracted to the area because of the great schools, good shopping, leisure facilities (parks, pools, courts etc), and excellent public and road transport infrastructure. Read the content of my e-book - it tells you every thing you need to know :)

Industry/Entity Type

Real Estate

Colors

Designer to choose colors to be used in the design.

Requirements
Must have
• Once completed the layout should not be too busy - it should be easy to read. I guess then the statement "less is more" is applicable.
• I will probably print a number of copies of this book for distribution as well - so please consider print attributes in the design.
• IMPORTANT: as for any e-book offering specialist advice, the MAIN reason for the book is for the generation of sales leads and to establish the author as a subject matter expert on the topic. Please consider this in your design elements. BUT - the book should also not come across as 1 big advertisement either. Subtle but impactful are well chosen words to describe how it should present.
Nice to have
• VARN Real Estate branding on every page - to re-inforce the message.
Should not have
• No need for animations or illustrations/

```html
<!DOCTYPE html>
<html lang="en">
<head>
<meta charset="utf-8">
<title>Property Presentation – VARN Real Estate</title>
<link href="https://fonts.googleapis.com/css2?family=Carlito:ital,wght@0,400;0,700;1,400;1,700&family=Montserrat:wght@800&display=swap" rel="stylesheet">
<style>
  :root {
    --navy: #2c4f86;
    --navy-dark: #26467a;
    --ink: #222222;
    --bar-grey: #a6a6a6;
    --quote-bg: #e6e6e6;
    --paper: #ffffff;
    --footer-ink: #dfe6f2;
  }
  * { box-sizing: border-box; margin: 0; padding: 0; }
  html, body { width: 849px; height: 1200px; overflow: hidden; background: var(--paper); }
  body { font-family: "Carlito", "Calibri", sans-serif; color: var(--ink); font-size: 14.3px; line-height: 20.6px; }
  .page { position: relative; width: 849px; height: 1200px; overflow: hidden; }
  .top-bar { position: absolute; top: 0; left: 0; width: 100%; height: 32px; background: var(--bar-grey); }

  .section-number {
    position: absolute; left: 76px; top: 128px; width: 72px; height: 72px; border-radius: 50%;
    background: var(--navy); color: #fff; font-family: "Montserrat", sans-serif; font-weight: 800;
    font-size: 22px; display: flex; align-items: center; justify-content: center;
  }
  .section-title {
    position: absolute; left: 165px; top: 126px;
    font-family: "Montserrat", sans-serif; font-weight: 800; font-size: 31px; line-height: 34px; letter-spacing: 0.3px; color: #111;
  }
  .section-lede { position: absolute; left: 165px; top: 160px; width: 610px; font-style: italic; font-size: 14.3px; line-height: 20.5px; }

  .block { position: absolute; text-align: justify; }
  .block p { margin-bottom: 9.5px; }
  .intro { left: 76px; top: 232px; width: 696px; }

  .pull-quote {
    position: absolute; left: 76px; top: 493px; width: 279px; height: 186px; background: var(--quote-bg);
    padding: 25px 24px 0 24px; font-style: italic; font-size: 14.3px; line-height: 20.6px;
  }
  .quote-side { left: 368px; top: 490px; width: 404px; }
  .wide-a { left: 76px; top: 690px; width: 696px; }

  .col-left { left: 76px; top: 763px; width: 323px; }
  .col-right { left: 448px; top: 763px; width: 324px; }
  .subhead { font-weight: 700; font-style: italic; margin-bottom: 10px; }

  .footer { position: absolute; left: 0; bottom: 0; width: 100%; height: 105px; background: var(--navy); color: var(--footer-ink); }
  .footer-contact { position: absolute; left: 76px; top: 32px; font-size: 12px; line-height: 18px; }
  .footer-contact em { font-style: italic; }
  .brand { position: absolute; left: 370px; top: 30px; width: 110px; text-align: center; color: #fff;
    font-family: "Carlito", sans-serif; font-weight: 700; font-size: 32px; line-height: 34px; letter-spacing: 2px; }
  .brand-sub { position: absolute; left: 370px; top: 65px; width: 110px; text-align: center; color: #fff; font-size: 6.5px; letter-spacing: 3.2px; }
  .page-count { position: absolute; right: 77px; top: 42px; font-size: 15px; color: #fff; }
  .page-count b { font-weight: 700; }
</style>
</head>
<body>
<div class="page">
  <div class="top-bar"></div>

  <div class="section-number">1</div>
  <h1 class="section-title">PROPERTY PRESENTATION:</h1>
  <p class="section-lede">Like any product – the newer, the cleaner, the shinier, and the better presented a property is for sale…then the more interest it will attract from prospective Buyers.</p>

  <div class="block intro">
    <p>The more Buyer interest that a property attracts…the more competition around the purchase price that will be created.</p>
    <p>And Buyer competition is fantastic if you know how to harness it to achieve the best possible sale price. But where is it that you should begin and how?</p>
    <p>So let’s start at the very beginning – property preparation and presentation for sale.</p>
    <p>It is important to state that very few people actually live in the manner that a house is presented for sale. In most instances what you see at homes that are open for Buyer inspection is the end result of a lot of hard work on behalf of the Vendor and others.</p>
    <p>So don’t be concerned – how ever and whatever your home looks like now…it can be transformed to maximize its appeal to Buyers.</p>
  </div>

  <blockquote class="pull-quote">“Vendor’s will always see all of the great and wonderful aspects of their property in an effort to create value and push up the price; a Buyer will always tell you everything that is wrong in an effort to drive down the price.”</blockquote>

  <div class="block quote-side">
    <p>The whole process of buying and selling property is very psychological and highly emotional for most people, so it is very important for Vendors to place themselves in the shoes of a Buyer when running a critical eye across the presentation preparations.</p>
    <p>Your property should be polished, displayed and presented to the highest possible standard. That standard will be different for everyone – factoring in age, ability, financial capacity, the size of family, number of pets and so on.</p>
  </div>

  <div class="block wide-a">
    <p>In addition - every property is different, and every property has it’s own features and personality – what’s important is to amplify the positives and minimize the impact of the negatives throughout the home.</p>
    <p>Let’s look at some of the basics:</p>
  </div>

  <div class="block col-left">
    <p class="subhead">Curbside appeal</p>
    <p>First impressions count - stand outside at the front of your house on the street and look at your house with a critical eye. Does your home stand out as a welcoming and “happy” place to arrive at?</p>
    <p>Tidy the gardens, mow the lawns, repair the gutters, paint under the eaves of the roof, clean the windows, repair the cracks in the cement driveways and do some basic landscaping such as adding mulch to garden beds (my personal preference for mulch is black tan bark – but other varieties are just as effective). You will find all these tasks make a huge difference to the exterior look and feel of your property.</p>
  </div>

  <div class="block col-right">
    <p>If your property has a fence, then clean it and paint it. Cut back any overgrown trees and bushes, trim and shape the edges of pathways, and clear and remove all rubbish (including rubbish bins) from the front of the house.</p>
    <p>By improving your properties curbside appeal and street presence you will not only allow Buyers to have an immediate positive first impression – you are also ensuring that the property is ready to be photographed for the all important exterior façade shot as part of the marketing and advertising.</p>
    <p class="subhead">Cleaning and de-cluttering</p>
    <p>If you have been living in your home for any more than a few years, then you might be surprised at</p>
  </div>

  <footer class="footer">
    <div class="footer-contact">Visit us at <em>www.varnhomesales.com</em><br>For more information</div>
    <div class="brand">VARN</div>
    <div class="brand-sub">REAL ESTATE</div>
    <div class="page-count">Page <b>2</b> of <b>3</b></div>
  </footer>
</div>
</body>
</html>
```